Design Project - Finance Website (Only need PSD)

UPDATED PROJECT (Now only PSD needed)
Need a Pressline design for a company called "Tavernor Brook Finance". The company provides finance for corporate clients, businesses and property developers. The design should be business like with appealing colours that communicate trust. I have uploaded a banner and logo to be incorporated or feel free to design something better if you think you can.
** I now only need the PSD
** I want something that is actually designed rather than from a template.
Thanks
Updates
The website will be used for lead generation so the contact form with adjustable fields in the Pressline backend should be fairly prominent on the page.
I have uploaded a banner and logo for the site. None of the designs I have seen so far were good enough so the first decent design using the new banner and logo provided will win the job. I do not want just a template that has been cut and paste from somewhere else, I want decent design. If anyone provides a decent design then I will give an extra bonus of $150.
Reason: I have uploaded a banner and logo for the site. None of the designs I have seen so far were good enough so the first decent design using the new banner and logo provided will win the job. I do not want just a template that has been cut and paste from somewhere else, I want decent design. If anyone provides a decent design then I will give an extra bonus of $150.
Thanks
Target Market(s)
Business owners & property developers
Industry/Entity Type
Finance
Requirements
Must have
- Contact form on home page that can be altered through the back end eg. ability to add or remove fields. Widgetised sidebars.
Nice to have
- Widgetised footer.

```html
<!DOCTYPE html>
<html lang="en">
<head>
<meta charset="utf-8">
<title>Tavernor Brook Finance</title>
<link href="https://fonts.googleapis.com/css2?family=Open+Sans:wght@400;600;700&display=swap" rel="stylesheet">
<style>
:root{
  --navy:#0a2a6e;
  --blue:#0d3d9b;
  --blue-text:#14479e;
  --red:#d91b24;
  --red-dark:#a90f16;
  --grey-bg:#f2f2f2;
  --card:#e3e3e3;
  --text:#555;
  --muted:#777;
  --white:#fff;
}
*{box-sizing:border-box;margin:0;padding:0}
html,body{width:912px;height:1200px;overflow:hidden}
body{position:relative;background:var(--grey-bg);font-family:"Open Sans",Arial,sans-serif;color:var(--text)}
.abs{position:absolute}

.header-band{left:0;top:0;width:912px;height:146px;background:linear-gradient(180deg,#05122e 0%,#0b2c72 60%,#1d4fb3 100%)}
.header-band::after{content:"";position:absolute;left:0;right:0;bottom:0;height:4px;background:var(--blue)}

.logo-tab{left:137px;top:0;width:79px;height:88px;background:var(--white);border-radius:0 0 12px 12px;box-shadow:0 2px 4px rgba(0,0,0,.3);display:flex;flex-direction:column;align-items:center;justify-content:flex-end;padding-bottom:10px;text-align:center}
.logo-mark{width:22px;height:22px;background:var(--blue);margin-bottom:6px}
.logo-name{font-size:10px;line-height:11px;font-weight:700;color:var(--blue)}

.main-nav{left:122px;top:128px;height:18px;display:flex;gap:2px}
.main-nav a{display:block;height:18px;padding:0 8px;font-size:8px;line-height:18px;color:#888;background:#d6d6d6;text-decoration:none}
.main-nav a.is-active{background:var(--white);color:var(--blue);font-weight:700}

.account-bar{left:641px;top:2px;width:148px;height:28px;background:var(--red);border:2px solid #f0f0f0;border-radius:2px;display:flex;box-shadow:0 1px 3px rgba(0,0,0,.5)}
.account-bar span{flex:1;color:var(--white);font-size:10px;line-height:24px;text-align:center}
.account-bar span+span{border-left:1px solid rgba(255,255,255,.5)}
.login-panel{left:585px;top:40px;width:197px;height:106px;background:#e9e9e9;border:1px solid #ccc;padding:14px 14px 0}
.login-panel .field{height:20px;background:var(--white);border:1px solid #aaa;font-size:8px;color:#888;line-height:18px;padding-left:5px;margin-bottom:8px}
.login-panel .row{display:flex;justify-content:space-between;align-items:center;margin-top:2px}
.login-panel .forgot{font-size:8px;color:#333}
.login-panel .btn{background:var(--red);color:var(--white);font-size:10px;font-weight:700;padding:3px 12px;border:1px solid var(--red-dark)}

.page{left:107px;top:146px;width:697px;height:962px;background:var(--white)}

.hero{left:122px;top:156px;width:669px;height:243px;border:1px solid #c8cde0;background:var(--white);box-shadow:0 6px 8px -4px rgba(0,0,0,.25)}
.lead-form{left:0;top:0;width:186px;height:195px;background:var(--blue);padding:4px 4px 0}
.form-box{position:relative;height:61px;background:var(--white);margin-bottom:4px;display:flex;align-items:flex-end;justify-content:center;padding-bottom:10px}
.form-box .tab{position:absolute;top:0;left:50%;transform:translateX(-50%);background:var(--blue);color:var(--white);font-size:10px;font-weight:600;padding:1px 8px 2px;border-radius:0 0 4px 4px;white-space:nowrap}
.form-box .input{width:140px;height:20px;border:1px solid #aaa;box-shadow:inset 0 1px 2px rgba(0,0,0,.2)}
.hero-copy{left:198px;top:54px}
.hero-kicker{font-size:10px;color:var(--blue-text);letter-spacing:-.3px}
.hero-kicker svg{display:block;margin-top:1px}
.hero-title{font-size:18px;line-height:21px;color:var(--blue-text);letter-spacing:-.8px;margin-top:6px;width:180px}
.hero-title b,.hero-sub b{font-weight:700}
.hero-sub{font-size:13px;color:var(--blue);letter-spacing:-.6px;margin-top:6px}
.hero-photo{left:370px;top:18px;width:290px;height:170px;background:radial-gradient(ellipse at 55% 55%,#e7b993 0%,#d79c74 28%,#f3eae4 60%,var(--white) 80%)}
.slider-arrows{left:632px;top:180px;display:flex;gap:2px}
.slider-arrows span{width:12px;height:11px;background:#2e6bd0;display:block}
.hero-bar{left:0;top:195px;width:667px;height:47px;background:var(--blue)}
.send-btn{left:51px;top:9px;width:92px;height:29px;background:linear-gradient(#ef3a3a,#c4121a);border:2px solid #eee;color:var(--white);font-size:10px;text-align:center;line-height:25px;letter-spacing:.5px}
.hero-bar .tagline{left:214px;top:14px;font-size:13px;color:var(--white);letter-spacing:-.7px}
.hero-bar .apply{left:506px;top:12px;font-size:15px;font-weight:700;color:var(--white);display:flex;align-items:center;gap:8px}
.apply-icon{width:24px;height:20px;background:var(--red);border:2px solid #fff;display:flex;align-items:center;justify-content:center}

.card{top:421px;width:215px;height:211px;background:var(--card);border-radius:0 0 4px 4px}
.card .tab{position:absolute;left:0;top:0;width:108px;height:22px;background:linear-gradient(#2f66c5,var(--blue));color:var(--white);font-size:11px;line-height:22px;padding-left:8px;border-radius:3px 3px 0 0}
.card .visual{position:absolute;left:0;top:22px;width:215px;height:87px;border-radius:0 8px 8px 0}
.card .visual.house{background:linear-gradient(90deg,var(--white) 35%,#c9a58a 65%,#8a6246 100%)}
.card .visual.isa{background:linear-gradient(90deg,var(--white) 30%,#d8a585 62%,#7b3c22 100%)}
.card .visual.cred{background:linear-gradient(90deg,var(--white) 25%,#a9b4c4 60%,var(--navy) 100%)}
.card .rate{position:absolute;left:7px;top:30px;color:var(--blue)}
.rate .pre{font-size:12px}
.rate .num{font-size:40px;font-weight:700;line-height:36px;letter-spacing:-2px;display:inline-block}
.rate .pct{display:inline-block;vertical-align:top;font-size:7px;line-height:8px;margin-top:4px}
.rate .pct b{font-size:16px;line-height:14px;display:block}
.card p{position:absolute;left:7px;width:203px;font-size:10px;line-height:13px;color:#333}
.card .blurb{top:113px}
.card .note{top:155px}
.card .btn{position:absolute;right:10px;top:182px;background:var(--red);color:var(--white);font-size:8px;font-weight:700;padding:2px 5px;border:1px solid #fff;box-shadow:0 0 0 1px var(--red-dark)}

.divider-h{left:200px;top:641px;width:520px;height:6px;background:radial-gradient(ellipse at center,rgba(0,0,0,.18),transparent 70%)}

.sidebar{left:137px;top:651px;width:150px}
.sidebar ul{list-style:none;margin-bottom:16.4px}
.sidebar li{font-size:7.5px;line-height:16.5px;color:#777;padding-left:8px;position:relative}
.sidebar li::before{content:"";position:absolute;left:0;top:7px;width:3px;height:3px;border-radius:50%;background:var(--blue)}
.divider-v{left:295px;top:649px;width:1px;height:445px;background:#ccc}

.content{left:308px;top:653px;width:482px}
.content p{font-size:8.7px;line-height:12px;color:#555;margin-bottom:13px}
.content h2{font-size:11.5px;font-weight:700;color:var(--blue-text);margin-bottom:12px}
.content h3{font-size:8.7px;font-weight:700;color:var(--blue-text);margin-bottom:11px}
.content p.small{font-size:7.3px;line-height:10px}

.footer{left:107px;top:1108px;width:697px;height:92px;background:var(--blue);color:var(--white);font-size:7.5px}
.footer .powered{left:10px;top:6px}
.footer .links{right:10px;top:6px;display:flex;gap:22px}
.footer .copy{left:0;right:0;top:69px;text-align:center}
</style>
</head>
<body>

<div class="abs header-band" role="img" aria-label="Night city skyline photograph in deep blues"></div>

<div class="abs logo-tab">
  <span class="logo-mark"></span>
  <span class="logo-name">Tavernor Brook<br>Finance</span>
</div>

<nav class="abs main-nav">
  <a href="#">About Us</a>
  <a href="#">Contact us</a>
  <a href="#" class="is-active">Mezzanine Finance</a>
  <a href="#">Privacy Policy</a>
  <a href="#">Terms and Conditions</a>
</nav>

<div class="abs account-bar"><span>&#9666;&nbsp; SIGNUP</span><span>LOGIN &nbsp;&#9656;</span></div>
<div class="abs login-panel">
  <div class="field">Username</div>
  <div class="field">Password</div>
  <div class="row"><span class="forgot">Forgot password?</span><span class="btn">Login</span></div>
</div>

<div class="abs page"></div>

<section class="abs hero">
  <form class="abs lead-form">
    <div class="form-box"><span class="tab">Your Name</span><span class="input"></span></div>
    <div class="form-box"><span class="tab">Your Number</span><span class="input"></span></div>
    <div class="form-box"><span class="tab">Your Company</span><span class="input"></span></div>
  </form>
  <div class="abs hero-copy">
    <div class="hero-kicker">Mezzanine Finance
      <svg width="92" height="6" viewBox="0 0 92 6"><path d="M2 5 Q46 -1 90 2" stroke="#d91b24" stroke-width="1.5" fill="none"/></svg>
    </div>
    <div class="hero-title"><b>Compare</b> several capital provider rates</div>
    <div class="hero-sub"><b>Optimise</b> your capital returns</div>
  </div>
  <div class="abs hero-photo" role="img" aria-label="Photograph of a business handshake"></div>
  <div class="abs slider-arrows"><span></span><span></span></div>
  <div class="abs hero-bar">
    <div class="abs send-btn">SEND &nbsp;&#9656;</div>
    <div class="abs tagline">Access to real estate and <b>hedge funds</b></div>
    <div class="abs apply">Look &amp; Apply
      <span class="apply-icon"><svg width="8" height="10" viewBox="0 0 8 10"><path d="M0 0 L8 5 L0 10Z" fill="#fff"/></svg></span>
    </div>
  </div>
</section>

<article class="abs card" style="left:129px">
  <div class="tab">LOANS</div>
  <div class="visual house" role="img" aria-label="Photograph of a hand holding a model house"></div>
  <div class="rate"><div class="pre">Just</div><span class="num">6.3</span><span class="pct"><b>%</b>APR<br>Representative</span></div>
  <p class="blurb">Whatever you're planning, you could make it happen with a great low rate. 6.3% APR Representative.</p>
  <p class="note">For main ClearAccount customers.</p>
  <span class="btn">&#9656; Look &amp; Apply</span>
</article>

<article class="abs card" style="left:349px">
  <div class="tab">ONLINE ISA</div>
  <div class="visual isa" role="img" aria-label="Photograph of a smiling customer"></div>
  <div class="rate"><div class="pre">Transfer to a great rate</div><span class="pct" style="margin-top:8px"><b style="font-size:8px">Up to</b></span> <span class="num">3.10</span><span class="pct"><b>%</b>APR<br>Representative</span></div>
  <p class="blurb">Whatever you're planning, you could make it happen with a great low rate. 6.3% APR Representative.</p>
  <p class="note">For main ClearAccount customers.</p>
  <span class="btn">&#9656; Look &amp; Apply</span>
</article>

<article class="abs card" style="left:569px">
  <div class="tab">CREADIT CARD</div>
  <div class="visual cred" role="img" aria-label="Photograph of a hand holding a payment card"></div>
  <div class="rate"><div class="pre">Just</div><span class="num">6.3</span><span class="pct"><b>%</b>APR<br>Representative</span></div>
  <p class="blurb">Whatever you're planning, you could make it happen with a great low rate. 6.3% APR Representative.</p>
  <p class="note">For main ClearAccount customers.</p>
  <span class="btn">&#9656; Look &amp; Apply</span>
</article>

<div class="abs divider-h"></div>

<aside class="abs sidebar">
  <ul>
    <li>Mezzanine Debt UK</li><li>Mezzanine Debt Financing</li><li>Mezzanine Finance UK</li><li>Mezzanine Finance 2012</li><li>Providers</li><li>Mezzanine Funding</li><li>Mezzanine Financing Rates</li><li>Mezzanine Property Finance</li>
  </ul>
  <ul>
    <li>Mezzanine Debt UK</li><li>Mezzanine Debt Financing</li><li>Mezzanine Finance UK</li><li>Mezzanine Finance 2012</li><li>Choosing Between Mezzanine Finance</li><li>Providers</li><li>Mezzanine Funding</li><li>Mezzanine Financing Rates</li><li>Mezzanine Property Finance</li>
  </ul>
  <ul>
    <li>Mezzanine Debt UK</li><li>Mezzanine Debt Financing</li><li>Mezzanine Finance UK</li><li>Mezzanine Finance 2012</li>
  </ul>
</aside>

<div class="abs divider-v"></div>

<main class="abs content">
  <p>Mezzanine finance is a method of raising capital that is financed by debt. It fills the gap in a company's finance structure between equity and senior debt. This means that mezzanine financing has priority over the company's equity but is subordinate to the debts of senior lenders. A mezzanine debt may have several specific structures such as a convertible preferred debt, private securities and second-lien debt.</p>
  <h2>MEZZANINE FINANCE BENEFITS</h2>
  <p>A company must have a positive cash flow to use mezzanine financing. It is typically used to expand the company through leveraged buyouts, recapitalization and acquisitions. The common feature of these types of mezzanine financing is that they offer a risk/return ratio that is lower than that of equity, but greater than that of debt. Borrowers usually consider mezzanine financing after a senior lender is no longer willing to make additional loans. However, the company's financial structure must still have the capacity for additional long-term loans. Mezzanine financing is often combined with senior debt to reduce the amount of equity that the borrowing company must give to the lender.</p>
  <h2>MEZZANINE FINANCE USES</h2>
  <p>A company may use mezzanine finance for a variety of specific purposes. This includes growth opportunities such as the expansion of a plant, a new distribution channel, a new product or the acquisition of a property. The managers of a company may also use this type of financing to buy out the owners of the company as part of a succession or exit strategy. The capital provided by mezzanine financing in these scenarios is typically a small portion of the total capital available to the company. However, mezzanine financing is essential for corporate expansion and succession planning.</p>
  <h2>MEZZANINE FUNDING GAP</h2>
  <p>The funding gap between equity and senior debt is the primary reason for using mezzanine funding. This gap often occurs when accountants reduce the estimated value of a company's fixed assets, anticipating that the value of these assets will not be realized. Senior lenders may also be reluctant to use intangible assets as collateral, or they may wish to limit the company's risk from a particular source of income. The finance structure of some companies may also make the cost of equity prohibitively expensive.</p>
  <h3>LENDERS</h3>
  <p class="small">Senior lenders typically view mezzanine financing as borrowing equity, although mezzanine financing has several advantages over equity. Mezzanine financing has greater security since it takes precedence over equity in the finance structure. Borrowing additional equity also reduces the value of the existing shares of stock. The dilution of stock from mezzanine financing is limited, since most of the loan is made through interest payments.</p>
</main>

<footer class="abs footer">
  <div class="abs powered">Powered by Keystone, the drag and drop Pressline theme</div>
  <div class="abs links"><span>Administration Login</span><span>Go To Top</span></div>
  <div class="abs copy">Copyright &copy; 2012 Tavernor Brook Finance</div>
</footer>

</body>
</html>
```